Brindle Oak Racquet Club app

Design a sporting app that can, post news, post events, capture and show live scores, link at least 6 websites, other functions would be an advantage. Real tennis is also known as Royal tennis and Court tennis.
This would be like a sporting clubs app that gives live scores.

Colors

Designer to choose colors to be used in the design.

Requirements
Must have
• post news, post events, capture and show live scores, link at least 6 websites,
Nice to have
• Instructions on how to launch the app on apple and android

```html
<!DOCTYPE html>
<html lang="en">
<head>
<meta charset="utf-8">
<title>Brindle Oak Racquet Club — Events</title>
<link rel="stylesheet" href="https://fonts.googleapis.com/css2?family=Open+Sans:wght@400;600;700;800&display=swap">
<style>
  :root {
    --bg-top: #0d1fa6;
    --bg-mid: #1730c9;
    --bg-bottom: #0a1a8e;
    --ghost: rgba(60, 90, 230, 0.45);
    --white: #ffffff;
    --text-soft: #e9ecf6;
    --shade: rgba(8, 10, 30, 0.78);
  }
  * { box-sizing: border-box; margin: 0; padding: 0; }
  html, body { width: 1200px; height: 2596px; overflow: hidden; }
  body {
    font-family: "Open Sans", Arial, sans-serif;
    color: var(--white);
    background: linear-gradient(160deg, var(--bg-top) 0%, var(--bg-mid) 45%, var(--bg-bottom) 100%);
    position: relative;
  }
  .status-bar {
    position: absolute; top: 0; left: 0; right: 0; height: 90px;
    display: flex; justify-content: space-between; align-items: center;
    padding: 0 56px 0 70px;
  }
  .status-time { font-size: 26px; font-weight: 600; letter-spacing: 0.5px; }
  .status-icons { display: flex; gap: 14px; align-items: center; }
  .page-header { position: absolute; top: 150px; left: 0; right: 0; height: 160px; text-align: center; }
  .page-title-ghost {
    position: absolute; left: 0; right: 0; top: -10px;
    font-size: 170px; font-weight: 800; color: var(--ghost); letter-spacing: 6px; line-height: 1;
  }
  .page-title {
    position: relative; font-size: 98px; font-weight: 700; letter-spacing: 2px; line-height: 160px;
  }
  .event-list { position: absolute; top: 360px; left: 36px; width: 1132px; list-style: none; }
  .event-card {
    position: relative; height: 392px; margin-bottom: 48px;
    border-radius: 16px; overflow: hidden;
  }
  .event-photo { position: absolute; inset: 0; }
  .event-card::after {
    content: ""; position: absolute; inset: 0;
    background: linear-gradient(180deg, rgba(0,0,0,0) 35%, var(--shade) 100%);
  }
  .photo-wood-racquet { background: linear-gradient(100deg, #4a2416 0%, #8a4a32 45%, #b36a48 70%, #6e3422 100%); }
  .photo-ball-hand { background: linear-gradient(110deg, #6b8fb8 0%, #9fb4cc 40%, #c9a28c 62%, #5c7899 100%); }
  .photo-racquet-row { background: linear-gradient(90deg, #6b6479 0%, #9c93a6 35%, #b7aebb 55%, #7d6f80 100%); }
  .photo-court-player { background: linear-gradient(100deg, #4a4532 0%, #8a8160 40%, #a59a74 60%, #3e3826 100%); }
  .photo-wood-floor { background: linear-gradient(120deg, #3a1d14 0%, #7a4030 45%, #9c5a40 70%, #4a2418 100%); }
  .event-info { position: absolute; left: 40px; bottom: 40px; z-index: 1; }
  .event-date { font-size: 36px; font-weight: 700; line-height: 1.2; letter-spacing: 0.3px; }
  .event-summary { font-size: 27px; font-weight: 400; color: var(--text-soft); margin-top: 6px; }
</style>
</head>
<body>
  <header class="status-bar">
    <span class="status-time">9:41</span>
    <span class="status-icons">
      <svg width="34" height="22" viewBox="0 0 34 22" aria-label="Signal">
        <rect x="0" y="14" width="6" height="8" rx="1" fill="#fff"/>
        <rect x="9" y="10" width="6" height="12" rx="1" fill="#fff"/>
        <rect x="18" y="5" width="6" height="17" rx="1" fill="#fff"/>
        <rect x="27" y="0" width="6" height="22" rx="1" fill="#fff"/>
      </svg>
      <svg width="30" height="22" viewBox="0 0 30 22" aria-label="Wi-Fi">
        <path d="M15 21 L10 15 A8 8 0 0 1 20 15 Z" fill="#fff"/>
        <path d="M5 10 A14 14 0 0 1 25 10" stroke="#fff" stroke-width="3.5" fill="none" stroke-linecap="round"/>
        <path d="M1 5 A20 20 0 0 1 29 5" stroke="#fff" stroke-width="3.5" fill="none" stroke-linecap="round"/>
      </svg>
      <svg width="50" height="24" viewBox="0 0 50 24" aria-label="Battery">
        <rect x="1" y="1" width="43" height="22" rx="6" fill="none" stroke="#fff" stroke-opacity="0.5" stroke-width="2"/>
        <rect x="4" y="4" width="37" height="16" rx="3.5" fill="#fff"/>
        <rect x="46" y="8" width="3" height="8" rx="1.5" fill="#fff" fill-opacity="0.5"/>
      </svg>
    </span>
  </header>

  <section class="page-header">
    <div class="page-title-ghost" aria-hidden="true">EVENTS</div>
    <h1 class="page-title">EVENTS</h1>
  </section>

  <ul class="event-list">
    <li class="event-card">
      <div class="event-photo photo-wood-racquet" role="img" aria-label="Photo of a wooden real tennis racquet and ball on a timber floor"></div>
      <div class="event-info">
        <p class="event-date">25 DECEMBER 2019</p>
        <p class="event-summary">Lorem Ipsum is simply dummy text</p>
      </div>
    </li>
    <li class="event-card">
      <div class="event-photo photo-ball-hand" role="img" aria-label="Photo of a hand holding a stitched real tennis ball"></div>
      <div class="event-info">
        <p class="event-date">26 DECEMBER 2019</p>
        <p class="event-summary">Lorem Ipsum is simply dummy text</p>
      </div>
    </li>
    <li class="event-card">
      <div class="event-photo photo-racquet-row" role="img" aria-label="Photo of a row of real tennis racquets against a wall"></div>
      <div class="event-info">
        <p class="event-date">27 DECEMBER 2019</p>
        <p class="event-summary">Lorem Ipsum is simply dummy text</p>
      </div>
    </li>
    <li class="event-card">
      <div class="event-photo photo-court-player" role="img" aria-label="Photo of a player striking a ball on a real tennis court"></div>
      <div class="event-info">
        <p class="event-date">28 DECEMBER 2019</p>
        <p class="event-summary">Lorem Ipsum is simply dummy text</p>
      </div>
    </li>
    <li class="event-card">
      <div class="event-photo photo-wood-floor" role="img" aria-label="Photo of a racquet and ball resting on a wooden floor"></div>
      <div class="event-info">
        <p class="event-date">30 DECEMBER 2019</p>
        <p class="event-summary">Lorem Ipsum is simply dummy text</p>
      </div>
    </li>
  </ul>
</body>
</html>
```